Larkmoor Counseling

We need a postcard design for a Brooklyn based counseling service geared towards new parents. The postcard will be placed in pediatrician's offices, kids stores, and any place parents frequent. We would like to see designs that incorporate elements, fonts, textures, etc from the website (www.larkmoorcounseling-example.com) and some of the basic text used to describe the business.

I've included a copy of the logo, the font file we used to create the logo, and the main image from the index of the website, and the background texture.

Target Market(s)

New parents in Brooklyn.

Industry/Entity Type

Business

Requirements
Must have
• Contact info, website.
Should not have
• This postcard is for display and promotional purposes in doctor's offices and kid's toy/clothing stores.

It does not need an area for postage / address.

```html
<!DOCTYPE html>
<html lang="en">
<head>
<meta charset="utf-8">
<title>Larkmoor Counseling Postcard</title>
<link href="https://fonts.googleapis.com/css2?family=Arimo:wght@400&family=Josefin+Sans:wght@300&display=swap" rel="stylesheet">
<style>
  :root {
    --stage: #444646;
    --paper: #e6e2da;
    --panel: #efece6;
    --header: #ffffff;
    --ink: #3c3c3c;
    --ink-soft: #5f5f5f;
    --logo-ink: #1c1c1c;
    --accent: #e08a55;
    --photo-light: #d9c7a4;
    --photo-mid: #9c6b4e;
    --photo-dark: #5b3a2b;
    --overlay-text: #ffffff;
  }
  * { box-sizing: border-box; margin: 0; padding: 0; }
  html, body { width: 946px; height: 1200px; overflow: hidden; }
  body { background: var(--stage); font-family: "Arimo", Arial, sans-serif; color: var(--ink); position: relative; }

  .postcard {
    position: absolute; left: 117px; width: 730px; overflow: hidden;
    background: var(--paper);
    box-shadow: 0 2px 10px rgba(0,0,0,.45);
  }
  .postcard--front { top: 31px; height: 557px; }
  .postcard--back { top: 610px; height: 562px; }

  .brand-band {
    position: absolute; left: 0; right: 0; background: var(--header);
    display: flex; align-items: center; justify-content: center; gap: 12px;
  }
  .postcard--front .brand-band { top: 15px; height: 85px; }
  .postcard--back .brand-band { top: 14px; height: 74px; }
  .brand-dot { width: 34px; height: 34px; border-radius: 50%; background: var(--logo-ink); }
  .postcard--back .brand-dot { width: 29px; height: 29px; }
  .brand-name {
    font-family: "Josefin Sans", Arial, sans-serif; font-weight: 300;
    color: var(--logo-ink); text-transform: uppercase; letter-spacing: 1px; line-height: 1;
  }
  .postcard--front .brand-name { font-size: 46px; }
  .postcard--back .brand-name { font-size: 39px; }

  .hero-photo {
    position: absolute; left: 0; right: 0; top: 100px; height: 287px;
    background: linear-gradient(100deg, var(--photo-light) 0%, #b98d6a 30%, var(--photo-mid) 55%, var(--photo-dark) 100%);
  }
  .hero-caption {
    position: absolute; right: 48px; top: 232px; text-align: right;
    font-family: "Josefin Sans", Arial, sans-serif; font-weight: 300; color: var(--overlay-text);
    text-shadow: 0 1px 3px rgba(0,0,0,.35);
  }
  .hero-caption__name { font-size: 32px; line-height: 1.15; margin-bottom: 4px; }
  .hero-caption__line { font-size: 15px; line-height: 25px; text-transform: uppercase; }

  .intro-panel {
    position: absolute; left: 29px; top: 387px; width: 669px; height: 123px;
    background: var(--panel); padding: 14px 17px 0 17px;
    font-size: 13.6px; line-height: 19.5px; color: var(--ink);
  }
  .intro-panel p + p { margin-top: 19px; }

  .contact { position: absolute; color: var(--ink); white-space: nowrap; }
  .postcard--front .contact { left: 0; right: 0; top: 549px; transform: translateY(-100%); text-align: center; font-size: 24px; }

  .services-panel {
    position: absolute; left: 29px; top: 88px; width: 672px; height: 459px; background: var(--panel);
  }
  .services-title {
    position: absolute; left: 18px; top: 15px; font-size: 24px; color: var(--accent); font-weight: 400;
  }
  .service { position: absolute; top: 50px; }
  .service--individual { left: 18px; width: 300px; }
  .service--group { left: 357px; width: 285px; }
  .service__title { font-size: 16px; color: #111; font-weight: 400; margin-bottom: 14px; }
  .service p, .service li { font-size: 12.3px; line-height: 17.3px; color: var(--ink-soft); }
  .service p + p { margin-top: 17px; }
  .service ul { list-style: none; margin-top: 0; }
  .service li::before { content: "\2022\00a0"; }

  .group-photo {
    position: absolute; left: 358px; top: 220px; width: 279px; height: 167px;
    border: 3px solid #111; background: radial-gradient(ellipse at center, #fbf8f2 0%, #efe6da 60%, #d8cdbf 100%);
  }
  .postcard--back .contact { right: 60px; top: 516px; font-size: 17.5px; text-align: right; }
</style>
</head>
<body>
  <section class="postcard postcard--front">
    <header class="brand-band">
      <span class="brand-dot"></span>
      <span class="brand-name">Larkmoor Counseling</span>
    </header>
    <div class="hero-photo" role="img" aria-label="Photo of a sunlit row of brownstone houses with stoops and spring trees"></div>
    <div class="hero-caption">
      <div class="hero-caption__name">Nora Whitfield, LCSW</div>
      <div class="hero-caption__line">Larkmoor Counseling</div>
      <div class="hero-caption__line">In-Home Therapy for Parents</div>
    </div>
    <div class="intro-panel">
      <p>Nora Whitfield is a licensed clinical social worker with years of experience working with pregnant women, new moms &amp; dads, and couples struggling through the early parenting years.</p>
      <p>Since even getting out of the house with a newborn can feel like a struggle, Nora Whitfield will meet with parents in their home for therapy sessions.</p>
    </div>
    <div class="contact">nora@larkmoorcounseling-example.com | 646.555.0142</div>
  </section>

  <section class="postcard postcard--back">
    <header class="brand-band">
      <span class="brand-dot"></span>
      <span class="brand-name">Larkmoor Counseling</span>
    </header>
    <div class="services-panel">
      <h2 class="services-title">Larkmoor Counseling Services</h2>
      <article class="service service--individual">
        <h3 class="service__title">Individual and Couples Therapy</h3>
        <p>Nora Whitfield offers in-home therapy for new parents who need individual support as they adjust to parenthood and learn to balance new life stresses. She utilizes a short term model (6-12 sessions) with Cognitive<br>Behavioral Therapy, mindfulness techniques and supportive talk therapy. She will work with parents on changing negative thought patterns and learning new coping skills.</p>
        <p>Often times the stress of children can affect each parent as well as their relationship to each other.<br>Nora meets with couples to work through these relationship issues.</p>
        <p>Therapy may focus on:</p>
        <ul>
          <li>Pregnancy and postpartum depression</li>
          <li>Stress and anxiety</li>
          <li>Relationship changes</li>
          <li>Confidence building</li>
          <li>Balancing work and home life</li>
        </ul>
      </article>
      <article class="service service--group">
        <h3 class="service__title">Group Therapy</h3>
        <p>Mindfulness for Moms is an ongoing group to learn and practice mindfulness techniques. Mindfulness can help when you feel overwhelmed and emotions take over. It can keep you focused on the present and help create a stronger bond between you and your baby.</p>
      </article>
      <div class="group-photo" role="img" aria-label="Photo of wooden chairs arranged in a circle for a group session"></div>
    </div>
    <div class="contact">nora@larkmoorcounseling-example.com | 646.555.0142</div>
  </section>
</body>
</html>
```